Startup Consultancy - Brochure Design

This needs to be a digital and potential hardcopy of a glossy brochure, designed to really catch the eye of prospective clients and draw them in. I am looking for something alternative from the "usual", but equally in keeping with the IT industry that the business operate in. The business specifically focuses on Print & Document Software and Technology solutions, and this should be considered in the design.

Target Market(s)

SMB and Corporate End Users, + Technology Resellers

Industry/Entity Type

Information Technology

Other font styles liked:
• Avenir

Colors
9d9d9d
848484
c3c3c3
e8e8e8
ffffff
eaeaea
0255a3
3176b5
85acd3

Requirements
Must have
• Company logo displayed on the front, plus any other relevant placements in pages
• Must follow the colour/style in some way of the website (www.brantwellconsultancy.co.uk)
Nice to have
• Some kind of infographical style in the brochure would be good, perhaps around the service listings

```html
<!DOCTYPE html>
<html lang="en">
<head>
<meta charset="utf-8">
<title>Brantwell Strategic Consultancy – Brochure</title>
<link rel="stylesheet" href="https://fonts.googleapis.com/css2?family=Mulish:wght@400;600;700;800&family=Saira:wght@600&display=swap">
<style>
:root{
  --stage:#a3a3a3;
  --paper:#ffffff;
  --charcoal:#58585a;
  --mid-grey:#9d9d9d;
  --light-grey:#c3c3c3;
  --mist:#e8e8e8;
  --ink:#333333;
  --body:#555555;
  --blue-deep:#0255a3;
  --blue:#3176b5;
  --blue-soft:#85acd3;
}
*{box-sizing:border-box;margin:0;padding:0}
html,body{width:1200px;height:1200px;overflow:hidden}
body{background:var(--stage);position:relative;font-family:"Mulish",sans-serif;color:var(--body)}
.spread{position:absolute;left:233px;width:733px;height:519px;background:var(--paper);overflow:hidden}
.spread--cover{top:54px}
.spread--inside{top:626px}
.abs{position:absolute}

/* cover: front page */
.brand-mark{left:29px;top:54px;width:70px;text-align:center}
.brand-mark__dot{display:block;width:14px;height:14px;border-radius:50%;background:var(--charcoal);margin:0 auto 4px}
.brand-mark__name{font-weight:800;font-size:13px;color:var(--charcoal);line-height:1}
.brand-mark__sub{font-weight:800;font-size:4px;color:var(--charcoal);letter-spacing:.3px}
.masthead{left:125px;top:42px}
.masthead__name{font-weight:800;font-size:24px;color:var(--charcoal);line-height:1}
.masthead__sub{font-weight:600;font-size:13px;letter-spacing:5.6px;color:var(--mid-grey);margin-top:4px}
.hero-strips{left:8px;top:148px;width:350px;height:202px}
.welcome{left:0;width:367px;top:356px;text-align:center;color:var(--blue-deep)}
.welcome__title{font-family:"Saira",sans-serif;font-weight:600;font-size:26px;line-height:1}
.welcome__sub{font-weight:700;font-size:14px;margin-top:4px}
.welcome__text{left:40px;width:287px;top:419px;text-align:center;font-size:12px;line-height:15px;color:var(--body)}

/* cover: back page */
.back-photo{left:367px;top:0;width:366px;height:519px}
.back-shapes{left:367px;top:0;width:366px;height:519px}
.back-brand{left:367px;width:366px;top:250px;text-align:center;color:#fff}
.back-brand__dot{display:block;width:18px;height:18px;border-radius:50%;background:#fff;margin:0 auto 6px}
.back-brand__name{font-weight:800;font-size:26px;line-height:1}
.back-brand__sub{font-weight:700;font-size:6px;letter-spacing:.6px;margin-top:2px}
.contact{left:367px;width:366px;top:358px;text-align:center;color:#fff}
.contact__title{font-weight:700;font-size:11.5px;margin-bottom:12px}
.contact__line{font-size:8.5px;line-height:11px;display:flex;justify-content:center;gap:4px;margin-bottom:4px}
.contact__line svg{width:8px;height:8px;flex:none;margin-top:1.5px}
.social{left:367px;width:366px;top:468px;display:flex;justify-content:center;gap:13px}
.social span{width:21px;height:21px;border-radius:3px;background:#fff}

/* inside */
.inside-photo{top:0;width:367px;height:190px}
.inside-photo--left{left:0}
.inside-photo--right{left:367px}
.section{top:150px;width:319px}
.section--about{left:24px}
.section--why{left:391px}
.section__title{font-weight:700;font-size:15px;color:var(--blue-deep);margin-bottom:18px}
.section__sub{font-weight:700;font-size:8.8px;color:var(--ink);line-height:10px}
.section p{font-size:7.6px;line-height:10.4px;color:var(--ink);text-align:justify;margin-bottom:10.4px}
.section p.lead{margin-top:0}
.footer-bands{left:0;top:0;width:733px;height:519px}
</style>
</head>
<body>

<section class="spread spread--cover">
  <div class="abs brand-mark">
    <span class="brand-mark__dot"></span>
    <div class="brand-mark__name">Brantwell</div>
    <div class="brand-mark__sub">STRATEGIC CONSULTANCY</div>
  </div>
  <div class="abs masthead">
    <div class="masthead__name">Brantwell Strategic</div>
    <div class="masthead__sub">CONSULTANCY LTD</div>
  </div>

  <svg class="abs hero-strips" viewBox="0 0 350 202" role="img" aria-label="Photo of colleagues' hands reviewing printed colour swatches and documents beside a laptop, shown through four slanted rounded strips">
    <defs>
      <linearGradient id="stripTone" x1="0" y1="0" x2="1" y2="1">
        <stop offset="0" stop-color="#d9d6d2"/>
        <stop offset=".45" stop-color="#c9bfb4"/>
        <stop offset=".75" stop-color="#7fa8c6"/>
        <stop offset="1" stop-color="#e9e7e4"/>
      </linearGradient>
    </defs>
    <g fill="url(#stripTone)">
      <rect x="10" y="-10" width="78" height="150" rx="39" transform="rotate(35 49 65)"/>
      <rect x="92" y="0" width="80" height="170" rx="40" transform="rotate(35 132 85)"/>
      <rect x="180" y="10" width="80" height="180" rx="40" transform="rotate(35 220 100)"/>
      <rect x="262" y="40" width="78" height="160" rx="39" transform="rotate(35 301 120)"/>
    </g>
  </svg>

  <div class="abs welcome">
    <div class="welcome__title">Welcome</div>
    <div class="welcome__sub">to a new approach</div>
  </div>
  <p class="abs welcome__text">We have a range of services suitable for a range of clients including End Users, Channel Partners, OEM’s and Distributors.</p>

  <div class="abs back-photo" role="img" aria-label="Faded photo of hands working on a laptop with light technology overlay" style="background:linear-gradient(180deg,#dfe5ec 0%,#eef1f4 45%,#f6f7f8 100%)"></div>
  <svg class="abs back-shapes" viewBox="0 0 366 519" preserveAspectRatio="none">
    <polygon points="0,215 96,242 0,279" fill="var(--light-grey)"/>
    <polygon points="0,279 366,160 366,519 0,519" fill="var(--charcoal)"/>
  </svg>

  <div class="abs back-brand">
    <span class="back-brand__dot"></span>
    <div class="back-brand__name">Brantwell</div>
    <div class="back-brand__sub">STRATEGIC CONSULTANCY</div>
  </div>

  <div class="abs contact">
    <div class="contact__title">Contact Us</div>
    <div class="contact__line"><svg viewBox="0 0 10 10"><rect width="10" height="10" rx="2" fill="#fff"/><path d="M3 2.5c.5 2.2 2 3.8 4.5 4.5l.5-1-1.3-.6-.5.6c-1-.5-1.7-1.2-2.2-2.2l.6-.5L4 2z" fill="#58585a"/></svg>0203 555 0147</div>
    <div class="contact__line"><svg viewBox="0 0 10 10"><rect x=".5" y="2" width="9" height="6.5" rx="1" fill="none" stroke="#fff"/><path d="M1 2.5l4 3 4-3" fill="none" stroke="#fff"/></svg>enquiries@brantwellconsultancy.co.uk</div>
    <div class="contact__line"><svg viewBox="0 0 10 10"><path d="M5 .5a3.2 3.2 0 0 0-3.2 3.2C1.8 6 5 9.5 5 9.5s3.2-3.5 3.2-5.8A3.2 3.2 0 0 0 5 .5z" fill="#fff"/><circle cx="5" cy="3.7" r="1.2" fill="#58585a"/></svg><span>48-52 Harrowgate Lane, London,<br>WC1X 4PL</span></div>
    <div class="contact__line"><svg viewBox="0 0 10 10"><circle cx="5" cy="5" r="4.3" fill="#fff"/><path d="M.8 5h8.4M5 .8c-2 2.5-2 5.9 0 8.4M5 .8c2 2.5 2 5.9 0 8.4" fill="none" stroke="#58585a" stroke-width=".7"/></svg>www.brantwellconsultancy.co.uk</div>
  </div>
  <div class="abs social"><span></span><span></span></div>
</section>

<section class="spread spread--inside">
  <div class="abs inside-photo inside-photo--left" role="img" aria-label="Faded photo of a colleague working at a laptop in a bright office" style="background:linear-gradient(180deg,#d7dde3 0%,#e6eaee 55%,#ffffff 100%)"></div>
  <div class="abs inside-photo inside-photo--right" role="img" aria-label="Faded photo of hands reviewing printed plans and blue colour swatches on a desk" style="background:linear-gradient(180deg,#d6d1cb 0%,#c9d6e2 50%,#ffffff 100%)"></div>

  <div class="abs section section--about">
    <h2 class="section__title">About Us</h2>
    <div class="section__sub">Taking a different path</div>
    <p class="lead">We provide services to End User organisations of various sizes, shapes and styles, ranging from SMB through to Enterprise business and even Government, across a range of vertical markets, helping to create forward thinking, future proofed strategic design for Print &amp; Document Workflow solutions - critically however as an entirely independent approach, without any affiliations to manufacturers, software houses or resellers.</p>
    <p>Our expertise, experience and services also support Channel Partners, OEM’s and Distributors, providing guidance and design services for Print &amp; Document Workflow strategies, promoting a customer led focus, efficiency and our own core values of honesty and reliability.</p>
    <p>As a group of very experienced, highly skilled and senior members of the IT/Print/Document Solutions industry, we grew tired of the lack of true, un-biased and trusted advice and support within the industry that both Channel Partners and End Users alike would often receive.</p>
    <p>We don’t sell hardware. We don’t even sell software.</p>
    <p>We remain independent of any manufacturers and are not affiliated to any partner or dealer. What we do provide however is trusted, valuable consultancy, design and advice.</p>
  </div>

  <div class="abs section section--why">
    <h2 class="section__title">Why Choose Us?</h2>
    <div class="section__sub">An alternative and innovative approach</div>
    <p class="lead">We take pride, satisfaction and enjoyment from providing clients with clear, non-bias advice. Our determination to stand alone in the industry without commercial affiliations or ties to ANY particular manufacturer, channel partner or software developers sets us apart from the rest.</p>
    <p>We consistently monitor the marketplace and industry, ensure we are up to speed on trends and technology as well as research and understanding, to deliver professional, experienced and justifiable advice and planning.</p>
    <p>We also maintain memberships with key industry analysts such as Northvale, Kestrel Research and more, along with having representation on European Advisory boards with a view to positively contributing to the imaging and printing industry standards.</p>
    <p>It is our aim to be the most trusted consultancy in our industry, but to do this we have to earn it.</p>
    <div class="section__sub" style="margin-bottom:10.4px">How do we do that?</div>
    <p>Honest and open advice, transparency in our approach and the integrity to ensure we inform our clients if we cannot provide services that are either suitable or to the high standards expected by you or us - if we can’t help we will tell you so openly, no fuss, no over promising.</p>
    <p>Our consultancy services also ensure you are aware and prepared for potential pitfalls, complexities and challenges associated with the world of Print &amp; Document solutions.</p>
  </div>

  <svg class="abs footer-bands" viewBox="0 0 733 519" preserveAspectRatio="none">
    <polygon points="0,484 178,490 0,501" fill="var(--blue)"/>
    <polygon points="733,484 555,490 733,501" fill="var(--blue)"/>
    <polygon points="0,501 178,490 367,475 555,490 733,501 733,519 0,519" fill="var(--charcoal)"/>
  </svg>
</section>

</body>
</html>
```